Hörbuchcover
Zielgruppe
Spiritueller Hörbuchverlag für ganzheitliche Gesundheit, Glück und Wohlstand.
Aufgabenstellung
Benötigt wird ein schönes quadratisches Cover, 2400x2400 mindestens 72dpi für ein Hörbuchcover.
Auf dem Cover soll eine gelb/orange Rose zu in Form einer Blüte zu sehen sein.
Titel: Innere Wandlung
Untertitel: Emotionen sind der Schlüssel für Gesundheit, Energie & Lebensfreude
Autorenname: Dr. med. Birgit Wolkenstein
Das Feloria Logo soll unten mittig sitzen.
Es folgen weiterer Hörbücher von dieser Autorin und es wäre gut wenn man die folgenden Cover in einem ähnlichen Stil halten könnte. Ein harmonisches und gut zu erkennendes Design mit hohem Wiedererkennungseffekt. Ich freue mich auf kreative Designvorschläge.
Auf feloria.de kann man sehen wo das Logo sitzen soll.
Herzliche Grüße - Jens

```html
<!DOCTYPE html>
<html lang="de">
<head>
<meta charset="utf-8">
<title>Innere Wandlung – Hörbuchcover</title>
<link rel="stylesheet" href="https://fonts.googleapis.com/css2?family=Cormorant+Garamond:ital,wght@1,500&family=Source+Sans+3:wght@400;600&display=swap">
<style>
  :root {
    --stage: #6b6b6b;
    --paper: #f6f5f1;
    --ink: #555552;
    --ink-dark: #1e1e1e;
    --title-start: #d9361c;
    --title-end: #f0661a;
    --ornament: rgba(160, 160, 156, 0.42);
    --ornament-fade: rgba(160, 160, 156, 0);
    --rose-light: #fbd43e;
    --rose-mid: #f59a1f;
    --rose-deep: #e6561a;
  }
  * { margin: 0; padding: 0; box-sizing: border-box; }
  html, body {
    width: 1104px; height: 1200px; overflow: hidden;
    background: var(--stage);
  }
  .cover {
    position: absolute; left: 103px; top: 151px;
    width: 900px; height: 900px;
    background: var(--paper);
    overflow: hidden;
  }
  .ornament-corner {
    position: absolute; top: -60px; width: 240px; height: 330px;
    border-radius: 50%;
  }
  .ornament-corner.left {
    left: -120px;
    background: radial-gradient(closest-side, var(--ornament), var(--ornament-fade));
  }
  .ornament-corner.right {
    right: -120px;
    background: radial-gradient(closest-side, var(--ornament), var(--ornament-fade));
  }
  .ornament-top {
    position: absolute; top: -40px; left: 150px; width: 600px; height: 90px;
    border-radius: 50%;
    background: radial-gradient(closest-side, var(--ornament), var(--ornament-fade));
  }
  .ornament-band {
    position: absolute; left: 0; top: 756px; width: 100%; height: 144px;
    background: linear-gradient(180deg, var(--ornament-fade) 0%, var(--ornament) 30%, var(--ornament) 85%, var(--ornament-fade) 100%);
  }
  .title {
    position: absolute; top: 42px; left: 0; width: 100%;
    text-align: center;
    font-family: "Cormorant Garamond", Georgia, serif;
    font-style: italic; font-weight: 500;
    font-size: 98px; line-height: 92px;
    background: linear-gradient(90deg, var(--title-start), var(--title-end));
    -webkit-background-clip: text; background-clip: text;
    color: transparent;
  }
  .subtitle {
    position: absolute; top: 250px; left: 0; width: 100%;
    text-align: center;
    font-family: "Source Sans 3", Arial, sans-serif;
    font-size: 39px; line-height: 46px;
    color: var(--ink);
  }
  .author {
    position: absolute; top: 370px; left: 0; width: 100%;
    text-align: center;
    font-family: "Source Sans 3", Arial, sans-serif;
    font-size: 41px; letter-spacing: 4px;
    color: var(--ink);
  }
  .rose {
    position: absolute; left: 200px; top: 420px;
    width: 526px; height: 410px;
    border-radius: 50%;
    background: radial-gradient(closest-side, var(--rose-light) 0%, var(--rose-mid) 45%, var(--rose-deep) 78%, rgba(230, 86, 26, 0) 100%);
  }
  .publisher {
    position: absolute; left: 0; bottom: 26px; width: 100%;
    display: flex; justify-content: center; align-items: center; gap: 12px;
    font-family: "Source Sans 3", Arial, sans-serif;
    font-weight: 600; font-size: 34px; letter-spacing: 3px;
    color: var(--ink-dark);
  }
  .publisher-dot {
    width: 22px; height: 22px; border-radius: 50%;
    background: var(--ink-dark);
  }
</style>
</head>
<body>
  <main class="cover">
    <div class="ornament-corner left" role="img" aria-label="Gezeichnete Blätterranke in der linken oberen Ecke"></div>
    <div class="ornament-top" role="img" aria-label="Blätterranke am oberen Rand"></div>
    <div class="ornament-corner right" role="img" aria-label="Gezeichnete Blätterranke in der rechten oberen Ecke"></div>

    <h1 class="title">Innere<br>Wandlung</h1>
    <p class="subtitle">Emotionen sind der Schlüssel für<br>Gesundheit, Energie &amp; Lebensfreude</p>
    <p class="author">Dr. med. Birgit Wolkenstein</p>

    <div class="ornament-band" role="img" aria-label="Florales Zierband am unteren Rand"></div>
    <div class="rose" role="img" aria-label="Gelb-orange Rosenblüte"></div>

    <div class="publisher"><span class="publisher-dot"></span>FELORIA</div>
  </main>
</body>
</html>
```